Our Pantry Remedy

I am a pharmacist turn chef and my current website www.ourpantryremedy-demo.com is in desperate need of a make over. I want to be able to add how to videos, photographs and have tabs. The tabs needed will be Home, About, Recipes, Health & Wellness, Services, Confidentiality, Affordability, Blog, Articles and Friday Cocktails. Eventually I will want a news letter, but do not want that now, only the ability to add it later. I will also want to add a market place tab later to sell merchandise and ebooks. The ability to navigate should be easy and not confusing and the ability to post should be easy. I will need social media Friendlyn, Clipboardia, searcho plus, searcho, Snapvue and chirpit. In addition I will need some direction on how to operate the site. Examples of website I like (but do not want to copy) are www.buildbrightvigor-demo.net www.drpaulvenmore-demo.com. It is best for me to work with someone who can explain things simply.
Updates

Another website I think is nice is www.zbgalley-demo.com  Thanks!

Target Market(s)

The business will be diving right into the delicious side of Key West’s good health as a personal chef, a culinary wellness coach, a wellness cooking teacher, a healthful caterer and a wellness host and entertainer.
The site needs to promote health with the art of food because I am convinced that health is best enhanced, maintained and recovered through nutritious eating and cuisine, and not through pills.
I will be infusing fresh recipes with a Key West flair in hopes to share my passion and insights into nutrition and health with residents and visitors alike. I want everyone to feel welcome to come in and join the fun.

Industry/Entity Type

Chef

Colors

Designer to choose colors to be used in the design.

Requirements
Must have
• Easy navigation, easy operation and posting and social media tools. Spam filters to keep the creeps away and important plugins that make it all work.
Nice to have
• Everything is nice to have

```html
<!DOCTYPE html>
<html lang="en">
<head>
<meta charset="utf-8">
<title>Our Pantry Remedy</title>
<link href="https://fonts.googleapis.com/css2?family=Ubuntu:wght@400;500&family=Arimo:wght@400&display=swap" rel="stylesheet">
<style>
:root{
  --orange:#f05a28;
  --green:#1f8a3d;
  --lime:#5aab1e;
  --slate:#393b43;
  --ink:#333;
  --body:#666;
  --band:#f1f2f2;
  --footer:#3c3c3c;
  --white:#fff;
}
*{margin:0;padding:0;box-sizing:border-box}
html,body{width:1138px;height:1200px;overflow:hidden;background:var(--white)}
body{position:relative;font-family:"Ubuntu",sans-serif;color:var(--ink)}
.abs{position:absolute}
.top-bar{left:0;top:0;width:1138px;height:4px;background:var(--orange)}
.brand{left:107px;top:12px;width:152px;height:88px;display:flex;flex-direction:column;align-items:center;justify-content:center;gap:8px}
.brand-name{font-size:20px;font-weight:500;color:var(--green)}
.brand-site{width:152px;height:18px;background:var(--orange);color:var(--white);font-size:9px;display:flex;align-items:center;justify-content:center}
.util-links{right:112px;top:12px;font-size:12px;color:#222;letter-spacing:.2px}
.util-links span{margin:0 8px}
.toll{left:660px;top:47px;font-size:12.5px;color:#333}
.toll b{font-weight:400;color:var(--orange);font-size:13.5px;margin-left:3px}
.social-top{left:898px;top:47px;display:flex;gap:6px;font-size:9.5px;color:#555}
.social-top span{display:flex;align-items:center;gap:2px}
.social-top i{width:6px;height:6px;background:#555;display:inline-block}
.nav{left:364px;top:67px;height:40px;display:flex;align-items:center}
.nav-home{width:46px;height:40px;background:var(--orange);display:flex;align-items:center;justify-content:center}
.nav a{color:var(--green);text-decoration:none;font-size:13.5px;margin-left:31px;padding-top:12px}
.nav a:first-of-type{margin-left:13px}
.hero{left:0;top:107px;width:1138px;height:393px;background:linear-gradient(100deg,#b9bdb5 0%,#c7472c 22%,#e9e2d5 45%,#d8cbb6 60%,#f2c020 78%,#d9381e 95%)}
.feature{left:104px;top:502px;width:929px;height:302px;background:var(--white);box-shadow:0 1px 6px rgba(0,0,0,.22)}
.feature-photo{left:13px;top:15px;width:329px;height:272px;background:linear-gradient(150deg,#d9cdbd,#b4772f 55%,#a3301e)}
.feature-title{left:368px;top:14px;width:285px;font-size:22px;font-weight:400;color:#333;padding-bottom:6px;border-bottom:3px solid #333}
.feature-copy{left:368px;top:66px;width:285px;font-family:"Arimo",sans-serif;font-size:11.6px;line-height:19px;color:var(--body)}
.feature-copy p{margin-bottom:12px}
.tabs{left:702px;top:15px;width:227px}
.tab{height:95px;background:var(--slate);color:var(--white);font-size:16.5px;display:flex;align-items:center;padding-left:40px;margin-bottom:1px;position:relative}
.tab.active{background:var(--orange)}
.tab.active::before{content:"";position:absolute;left:-14px;top:16px;border:14px solid transparent;border-left:0;border-right-color:var(--orange)}
.col-title{top:845px;font-size:24px;font-weight:500;color:var(--slate)}
.tile{top:877px;width:297px;height:155px;border:3px solid var(--lime)}
.tile-food{left:104px;background:linear-gradient(135deg,#c9a27a,#5a3a28 50%,#c5502a)}
.tile-video{left:421px;background:linear-gradient(135deg,#e6e6e4,#6f7b54 50%,#d9dad6);display:flex;align-items:center;justify-content:center}
.tile-blog{left:736px;background:var(--white)}
.blog-photo{left:12px;top:15px;width:82px;height:130px;background:linear-gradient(180deg,#eceae6,#c9b8a7 50%,#2f3034)}
.blog-name{left:111px;top:16px;font-size:14px;color:var(--orange)}
.blog-role{left:111px;top:37px;font-size:12px;color:var(--green)}
.blog-text{left:111px;top:68px;width:185px;font-size:11.5px;line-height:17px;color:#777;letter-spacing:.3px}
.blog-more{left:111px;top:130px;font-size:11px;color:var(--orange)}
.newsletter{left:0;top:1032px;width:1138px;height:90px;background:var(--band)}
.nl-label{left:248px;top:36px;display:flex;align-items:center;gap:12px;font-size:14px;color:#444}
.nl-input{left:477px;top:19px;width:267px;height:48px;background:var(--white);font-size:13px;color:#bbb;padding:18px 0 0 22px}
.nl-submit{left:763px;top:19px;width:134px;height:48px;background:var(--orange);color:var(--white);font-size:14px;display:flex;align-items:center;justify-content:center}
.footer{left:0;top:1122px;width:1138px;height:78px;background:var(--footer)}
.footer-note{left:0;top:22px;width:1138px;text-align:center;font-size:11.5px;color:var(--white)}
.footer-social{left:0;top:43px;width:1138px;display:flex;justify-content:center;gap:16px;font-size:10px;color:var(--white)}
.footer-social span{display:flex;align-items:center;gap:5px}
.footer-social i{width:20px;height:20px;border-radius:50%;background:var(--white);display:inline-block}
</style>
</head>
<body>
<div class="abs top-bar"></div>

<header>
  <div class="abs brand">
    <div class="brand-name">Chef Remy Calder</div>
    <div class="brand-site">OurPantryRemedy-demo.com</div>
  </div>
  <div class="abs util-links">Confidentiality<span>|</span>Affordability<span>|</span>Friday Cocktails</div>
  <div class="abs toll">Toll Free Numbers:<b>1800 000 111</b></div>
  <div class="abs social-top">
    <span><i></i>Linkora</span><span><i></i>chirpit</span><span><i></i>Friendlyn</span><span><i></i>Vidtube</span><span><i></i>searcho+</span>
  </div>
  <nav class="abs nav">
    <div class="nav-home" aria-label="Home">
      <svg width="18" height="16" viewBox="0 0 18 16"><path d="M9 1 1 8h2.5v7h4v-4.5h3V15h4V8H17Z" fill="#fff"/></svg>
    </div>
    <a>ABOUT</a><a>SERVICES</a><a>ARTICLES</a><a>RECIPES</a><a>HEALTH &amp; WELLNESS</a><a>BLOG</a><a>CONTACT</a>
  </nav>
</header>

<div class="abs hero" role="img" aria-label="Hands slicing mushrooms on a board beside tomatoes, herbs and a yellow pepper"></div>

<section class="abs feature">
  <div class="abs feature-photo" role="img" aria-label="Chef topping a pizza with cheese and olives"></div>
  <h2 class="abs feature-title">FRIDAY COCKTAILS</h2>
  <div class="abs feature-copy">
    <p>Lorem Ipsum is simply dummy text of the printing and typesetting industry. Lorem Ipsum has been the industry's standard dummy text ever since the 1500s, when an unknown printer took a galley of type and scrambled it to make a type specimen book.</p>
    <p>Lorem Ipsum is simply dummy text of the printing and typesetting industry. Lorem Ipsum has been the industry's standard dummy text ever since the 1500s, when an unknown printer took a galley of type and scrambled it to make a type specimen book.</p>
  </div>
  <div class="abs tabs">
    <div class="tab active">FRIDAY COCKTAILS</div>
    <div class="tab">CONFIDENTIALITY</div>
    <div class="tab">AFFORDABILITY</div>
  </div>
</section>

<h3 class="abs col-title" style="left:106px">WHAT’S NEW</h3>
<h3 class="abs col-title" style="left:422px">VIDEOS</h3>
<h3 class="abs col-title" style="left:737px">BLOG</h3>

<div class="abs tile tile-food" role="img" aria-label="Wrap filled with a burger patty, cucumber and tomato"></div>
<div class="abs tile tile-video" role="img" aria-label="Plated salads on white dishes, video thumbnail">
  <svg width="56" height="40" viewBox="0 0 56 40"><rect width="56" height="40" rx="8" fill="#111"/><path d="M22 11v18l15-9Z" fill="#fff"/></svg>
</div>
<div class="abs tile tile-blog">
  <div class="abs blog-photo" role="img" aria-label="Portrait of a young chef in a white hat"></div>
  <div class="abs blog-name">LENA BROOK HARLOW</div>
  <div class="abs blog-role">Jr. Chef</div>
  <div class="abs blog-text">Lorem Ipsum is simply dummy text of the printing and typesetting industry.</div>
  <div class="abs blog-more">Read More...</div>
</div>

<section class="abs newsletter">
  <div class="abs nl-label">
    <svg width="23" height="17" viewBox="0 0 23 17"><rect x="1" y="1" width="21" height="15" rx="2" fill="none" stroke="#444" stroke-width="1.6"/><path d="M1.5 2 11.5 10 21.5 2" fill="none" stroke="#444" stroke-width="1.6"/></svg>
    SIGN UP FOR NEWSLETTER
  </div>
  <div class="abs nl-input">YOUR EMAIL ADDRESS</div>
  <div class="abs nl-submit">SUBMIT</div>
</section>

<footer class="abs footer">
  <div class="abs footer-note">REMY CALDER © 2014 | PRIVACY POLICY</div>
  <div class="abs footer-social">
    <span><i></i>Friendlyn</span><span><i></i>chirpit</span><span><i></i>Clipboardia</span><span><i></i>Linkora</span>
  </div>
</footer>
</body>
</html>
```